Gordon Pellbrook Consulting - Web Design Project

We need a web design for my new edgy consulting business specializing in innovation, technology and strategy.

It is our personal goal to turn each client into raving fans by helping them achieve their own business goals and aspirations through assisting them in raising their own innovation and marketing standards.

We provide our personalised and state-of-the-art services to our clients and boards who represent some of the world greatest innovative thinkers.
Updates

Here is some other information which may help shape your thinking.

I've had direct Involvement in the development of the following iPad, iPhone Applications and websites

FarbeyondOzlands.com (TerraLink platform) by Voyage Bureau
http://farbeyondozlands.example.au

Sail Verve by Bright Voyaging
https://apps.example-store.com/au/app/sail-verve/id100000001

uRedlandTR by Travel Territory Board
https://apps.example-store.com/au/app/uredlandtr/id100000002

Wexmoor Trips
http://www.wexmoortrips.example.au

Trek Mapper by Voyage Bureau
http://apps.example-store.com/au/app/trek-mapper/id100000003

Sunward by Sunward Travel Office
https://apps.example-store.com/au/app/sunward/id100000004

Upper Fernridge Valley Route by Visit Coastlands
https://apps.example-store.com/au/app/upper-fernridge-valley-route/id100000005

Wanderer Path by Travel Territory Board and Southern Plains Travel Council
https://apps.example-store.com/au/app/wanderers-path-grand-journey/id100000006

Gordon Pellbrook Consulting (GPC)
November 2012 – Present (8 months)Brisbane, Sydney, Canberra

Gordon’s consults to Small-to-Medium Enterprises (SME) and Government organisations on business strategy, technology strategy, risk mitigation, disruptive technology and innovation in the workplace.

Gordon’s consultancy mantra is that we cannot divorce economic life from cultural life particularly in an era when social capital may be as important as physical capital in business.

Reason: request from designers, I want to see their best efforts

Target Market(s)

35+

Industry/Entity Type

Business

Requirements
Must have
• Please use some of the personal image(s) contained in the zip files which can be downloaded from here

http://filedrop.example/k9Xq2Lm
http://filedrop.example/p4Rt7Vn
http://filedrop.example/z8Hw3Bc
Nice to have
• Black, Sleek design, maybe minimalist. Nice to have a Pixelle for the design. Nice to have it easily ported to Wordpress or be a modified Wordpress template. HTML 5, responsive design

```html
<!DOCTYPE html>
<html lang="en">
<head>
<meta charset="utf-8">
<title>Gordon Pellbrook Consulting</title>
<link rel="stylesheet" href="https://fonts.googleapis.com/css2?family=Source+Sans+3:ital,wght@0,400;0,600;0,700;1,700&display=swap">
<style>
  :root {
    --ink: #000000;
    --text: #3f3f3f;
    --muted: #666666;
    --card: #ffffff;
    --backdrop-light: #f7f7f7;
    --backdrop-dark: #e6e6e6;
    --photo-light: #eef2e6;
    --photo-mid: #b9c6d4;
    --photo-dark: #7f93ab;
    --button-top: #ffffff;
    --button-bottom: #dcdcdc;
    --button-edge: #c4c4c4;
    --nav-start: #ffffff;
    --nav-end: #9a9a9a;
  }
  * { box-sizing: border-box; margin: 0; padding: 0; }
  html, body {
    width: 1200px;
    height: 602px;
    overflow: hidden;
  }
  body {
    position: relative;
    font-family: "Source Sans 3", "Myriad Pro", Arial, sans-serif;
    color: var(--text);
  }
  .backdrop {
    position: absolute;
    inset: 0;
    background: linear-gradient(135deg, var(--backdrop-light), var(--backdrop-dark) 50%, var(--backdrop-light));
  }
  .portrait {
    position: absolute;
    left: 123px;
    top: 76px;
    width: 320px;
    height: 480px;
    background: linear-gradient(160deg, var(--photo-light) 0%, var(--photo-mid) 55%, var(--photo-dark) 100%);
  }
  .card {
    position: absolute;
    left: 443px;
    top: 76px;
    width: 686px;
    height: 480px;
    background: var(--card);
    border: 2px solid var(--ink);
    border-left: none;
    border-top-right-radius: 92px;
  }
  .intro {
    position: absolute;
    left: 21px;
    top: 193px;
    width: 440px;
  }
  .intro-title {
    font-size: 26px;
    font-weight: 700;
    color: var(--ink);
    line-height: 30px;
    letter-spacing: 0.1px;
  }
  .intro-role {
    font-size: 24px;
    font-weight: 400;
    color: var(--muted);
    line-height: 30px;
  }
  .intro-text {
    margin-top: 12px;
    font-size: 13px;
    line-height: 17px;
    color: var(--text);
  }
  .social {
    position: absolute;
    left: 19px;
    top: 383px;
    display: flex;
    gap: 10px;
    list-style: none;
  }
  .social-link {
    display: flex;
    align-items: center;
    justify-content: center;
    width: 32px;
    height: 32px;
    border: 1px solid var(--button-edge);
    border-radius: 3px;
    background: linear-gradient(var(--button-top), var(--button-bottom));
    font-size: 10px;
    font-weight: 600;
    color: var(--muted);
    text-decoration: none;
  }
  .main-nav {
    position: absolute;
    left: 980px;
    top: 277px;
    list-style: none;
  }
  .nav-item + .nav-item { margin-top: 20px; }
  .nav-link {
    display: flex;
    align-items: center;
    width: 147px;
    height: 40px;
    padding-left: 10px;
    background: linear-gradient(90deg, var(--nav-start), var(--nav-end));
    color: var(--ink);
    text-decoration: none;
  }
  .nav-icon { width: 26px; height: 26px; flex: none; }
  .nav-label {
    flex: 1;
    text-align: center;
    padding-right: 4px;
    font-size: 18px;
    font-weight: 700;
    font-style: italic;
  }
  .site-footer {
    position: absolute;
    left: 464px;
    top: 571px;
    font-size: 12.5px;
    color: var(--ink);
  }
</style>
</head>
<body>
  <div class="backdrop" role="img" aria-label="Light grey diagonal chevron line pattern background"></div>

  <div class="portrait" role="img" aria-label="Portrait photograph of Gordon Pellbrook in a grey suit, seated by a bright window"></div>

  <main class="card">
    <section class="intro">
      <h1 class="intro-title">Gordon Pellbrook Consulting</h1>
      <p class="intro-role">Software Engineer</p>
      <p class="intro-text">Lorem ipsum dolor sit amet, consectetuer adipiscing elit, sed diam nonummy nibh euismod tincidunt ut laoreet dolore magna aliquam erat volutpat. Ut wisi enim ad minim veniam, quis nostrud exerci tation ullamcorper suscipit lobortis nisl ut aliquip ex ea commodo consequat.</p>
    </section>

    <ul class="social">
      <li><a class="social-link" href="#">Kin</a></li>
      <li><a class="social-link" href="#">Chirp</a></li>
      <li><a class="social-link" href="#">Mesh</a></li>
      <li><a class="social-link" href="#">Orb</a></li>
    </ul>
  </main>

  <nav>
    <ul class="main-nav">
      <li class="nav-item">
        <a class="nav-link" href="#">
          <svg class="nav-icon" viewBox="0 0 26 26" aria-hidden="true">
            <path d="M13 4 L2 13 L5 13 L5 22 L11 22 L11 16 L15 16 L15 22 L21 22 L21 13 L24 13 Z" fill="#000"/>
            <rect x="17" y="5" width="3" height="5" fill="#000"/>
          </svg>
          <span class="nav-label">Home</span>
        </a>
      </li>
      <li class="nav-item">
        <a class="nav-link" href="#">
          <svg class="nav-icon" viewBox="0 0 26 26" aria-hidden="true">
            <rect x="5" y="3" width="16" height="21" fill="none" stroke="#000" stroke-width="2"/>
            <circle cx="13" cy="11" r="3" fill="#000"/>
            <path d="M8 20 Q13 13 18 20 Z" fill="#000"/>
          </svg>
          <span class="nav-label">Profile</span>
        </a>
      </li>
      <li class="nav-item">
        <a class="nav-link" href="#">
          <svg class="nav-icon" viewBox="0 0 26 26" aria-hidden="true">
            <rect x="9" y="4" width="8" height="5" fill="none" stroke="#000" stroke-width="2"/>
            <rect x="2" y="8" width="22" height="15" rx="1" fill="none" stroke="#000" stroke-width="2.4"/>
            <rect x="2" y="13" width="22" height="2" fill="#000"/>
            <rect x="11" y="12" width="4" height="4" fill="#000"/>
          </svg>
          <span class="nav-label">Portfolio</span>
        </a>
      </li>
      <li class="nav-item">
        <a class="nav-link" href="#">
          <svg class="nav-icon" viewBox="0 0 26 26" aria-hidden="true">
            <rect x="1" y="5" width="24" height="17" rx="2" fill="#000"/>
            <rect x="6" y="3" width="2" height="4" fill="#000"/>
            <rect x="18" y="3" width="2" height="4" fill="#000"/>
            <circle cx="8" cy="12" r="2.5" fill="#fff"/>
            <path d="M4 19 Q8 13 12 19 Z" fill="#fff"/>
            <rect x="14" y="11" width="8" height="2" fill="#fff"/>
            <rect x="14" y="15" width="8" height="2" fill="#fff"/>
          </svg>
          <span class="nav-label">Contact</span>
        </a>
      </li>
    </ul>
  </nav>

  <footer class="site-footer">2012 © Gordon Pellbrook Consulting.com</footer>
</body>
</html>
```